Postcard Mailer

We are a pizza pub that is the only local restaurant that offers and delivers pizza, burgers, salads and wings.

We just opened and want to send out a postcard to the community. thinking on one side a nice design with pics etc. then on the back a list of our daily food and drink specials.

Restaurant

eb1f27

```html
<!DOCTYPE html>
<html lang="en">
<head>
<meta charset="utf-8">
<title>Marlow and Enzo – Postcard Mailer</title>
<link href="https://fonts.googleapis.com/css2?family=Bitter:wght@700&family=Staatliches&display=swap" rel="stylesheet">
<style>
  :root {
    --card-black: #000000;
    --accent-yellow: #f6e600;
    --ink-white: #ffffff;
  }
  html, body {
    margin: 0;
    width: 1200px;
    height: 952px;
    overflow: hidden;
    background: var(--card-black);
  }
  .postcard {
    position: relative;
    width: 1200px;
    height: 952px;
    background: var(--card-black);
    overflow: hidden;
  }
  .brand {
    position: absolute;
    left: 40px;
    top: 60px;
    width: 310px;
    text-align: center;
    color: var(--ink-white);
    font-family: "Staatliches", sans-serif;
  }
  .brand-mark {
    width: 56px;
    height: 56px;
    border-radius: 50%;
    background: var(--ink-white);
    margin: 0 auto 18px;
  }
  .brand-name {
    font-size: 48px;
    line-height: 1;
    letter-spacing: 1px;
  }
  .brand-web {
    font-size: 22px;
    margin-top: 14px;
    letter-spacing: 1px;
  }
  .brand-contact {
    font-size: 24px;
    line-height: 1.05;
    margin-top: 56px;
  }
  .headline {
    position: absolute;
    right: 34px;
    top: 52px;
    margin: 0;
    color: var(--accent-yellow);
    font-family: "Staatliches", sans-serif;
    font-size: 56px;
    font-weight: 400;
    letter-spacing: 2px;
  }
  .phone {
    position: absolute;
    right: 34px;
    top: 140px;
    display: flex;
    align-items: center;
    gap: 20px;
    color: var(--accent-yellow);
    font-family: "Staatliches", sans-serif;
    font-size: 56px;
    letter-spacing: 1px;
  }
  .phone svg { width: 46px; height: 46px; }
  .menu-list {
    position: absolute;
    left: 46px;
    top: 468px;
    margin: 0;
    padding: 0;
    list-style: none;
    color: var(--accent-yellow);
    font-family: "Bitter", serif;
    font-weight: 700;
    font-size: 56px;
    line-height: 74px;
  }
  .menu-list li::before {
    content: "";
    display: inline-block;
    width: 20px;
    height: 20px;
    border-radius: 50%;
    background: var(--accent-yellow);
    margin-right: 20px;
    vertical-align: middle;
  }
  .hero-photo {
    position: absolute;
    left: 380px;
    top: 230px;
    width: 820px;
    height: 722px;
  }
  .photo-strip {
    position: absolute;
    left: 0;
    top: 790px;
    width: 1200px;
    height: 162px;
  }
</style>
</head>
<body>
<main class="postcard">
  <div class="brand">
    <div class="brand-mark"></div>
    <div class="brand-name">Marlow and Enzo</div>
    <div class="brand-web">www.marlowenzo.com</div>
    <div class="brand-contact">Harborview, NC<br>555.014.2270</div>
  </div>

  <h1 class="headline">Visit Our Restaurant Today</h1>
  <div class="phone">
    <svg viewBox="0 0 46 46" aria-hidden="true">
      <circle cx="23" cy="23" r="20.5" fill="none" stroke="currentColor" stroke-width="3"/>
      <path d="M16 12c-2 1-3 3-3 5 1 7 8 15 16 16 2 0 4-1 5-3l-4-4-3 2c-3-1-6-4-7-7l2-3z" fill="none" stroke="currentColor" stroke-width="2.6" stroke-linejoin="round"/>
    </svg>
    <span>555 014 2270</span>
  </div>

  <ul class="menu-list">
    <li>Pizzas</li>
    <li>Burgers</li>
    <li>Wings</li>
    <li>Salads.</li>
  </ul>

  <svg class="hero-photo" viewBox="0 0 820 722" role="img" aria-label="Photo of a hand holding a veggie burger with avocado and lettuce on a wholegrain bun">
    <defs>
      <linearGradient id="heroTone" x1="0" y1="0" x2="0" y2="1">
        <stop offset="0" stop-color="#8a5a30"/>
        <stop offset="0.22" stop-color="#b98250"/>
        <stop offset="0.36" stop-color="#c27a3a"/>
        <stop offset="0.48" stop-color="#6f8f3a"/>
        <stop offset="0.58" stop-color="#b58a5c"/>
        <stop offset="0.75" stop-color="#d9a27f"/>
        <stop offset="1" stop-color="#c98f6c"/>
      </linearGradient>
      <radialGradient id="heroFade" cx="55%" cy="55%" r="62%">
        <stop offset="0.55" stop-color="#fff"/>
        <stop offset="1" stop-color="#000"/>
      </radialGradient>
      <mask id="heroMask">
        <rect width="820" height="722" fill="url(#heroFade)"/>
      </mask>
    </defs>
    <rect width="820" height="722" fill="url(#heroTone)" mask="url(#heroMask)"/>
  </svg>

  <svg class="photo-strip" viewBox="0 0 1200 162" role="img" aria-label="Photo strip of a bacon cheeseburger, a fresh salad and a mushroom pizza">
    <defs>
      <linearGradient id="burgerTone" x1="0" x2="1">
        <stop offset="0" stop-color="#3a2414"/><stop offset="1" stop-color="#8a5a2c"/>
      </linearGradient>
      <linearGradient id="saladTone" x1="0" x2="1">
        <stop offset="0" stop-color="#6f8f3a"/><stop offset="1" stop-color="#b8432c"/>
      </linearGradient>
      <linearGradient id="pizzaTone" x1="0" x2="1">
        <stop offset="0" stop-color="#b8452a"/><stop offset="1" stop-color="#d39a5a"/>
      </linearGradient>
    </defs>
    <polygon points="0,2 162,2 310,160 0,160" fill="url(#burgerTone)" stroke="#fff" stroke-width="3"/>
    <polygon points="175,2 490,2 638,160 323,160" fill="url(#saladTone)" stroke="#fff" stroke-width="3"/>
    <polygon points="503,2 795,2 943,160 651,160" fill="url(#pizzaTone)" stroke="#fff" stroke-width="3"/>
  </svg>
</main>
</body>
</html>
```